Small business offering independent forensic science consultancy requires flyer and magnet design

We had great success in obtaining a logo design using pixel harbor and we are hoping to draw on your expertise again!

Clearwater Evidence Advisors is a small consultancy business that mainly involves reviewing forensic case files for both the prosecution and defence, and providing expert opinion on the findings in the form of a report, as well as attending court as an expert witness.

Our areas of expertise currently is Forensic Biology (analysis of body fluids), DNA analysis and bloodstain pattern analysis, but this may grow in the future. You can find further information as well as obtain a bit of a feel for the style we are looking for from our website www.clearwaterevidenceadvisors.com.au.

The flyer should be clean and professional looking and we have attached files including our logo and and a Plumtree Text Doc containing the wording for inclusion in the flyer. We have attached an 'ímage feel' document to give you a feel for the types of images we like - but we own all the images on our website, so please contact me if you want to use any of these images and I can send you the files - however are open to any other images in keeping with our website and brand feel.

We will consider various format options such as tri-fold, bi-fold, however,DL sized bi-fold is probably a slight preference. We are also open to suggestions from designers. We would also like to have the capability to modify our wording on the flyer as we have not completely locked it in as yet.

Please note that the brief is also to include the design of a simple advertising magnet to supplement our flyers. They will also be given out separately. The magnet should be a simple design for standard size (90mm x 45mm) magnet, similar to a business card with logo, tagline and contact details (information contained in attached file).

We look forward to seeing your design ideas. Thanks!
Updates

We will be extending the deadline for this project to the 10th January, to allow designers plenty of time given the time of year! 

Thanks to all the designers who have submitted designs so far - as it is the Christmas and New Year period, I will be extending the deadline by one week to allow time for all of you who have accepted my invitation to submit a design.

We will provide individual feedback over the next week to those who have submitted designs. 

We've had some great designs so far - and look forward to seeing some more!

Many thanks!

Hi designers - thanks for the designs submitted so far.  We have provided feedback to all designs under consideration - and welcome re-submissions with the alterations we have suggested.

The deadline will stay at the 10th Jan, so please finalise your designs and re-submit before this date.

We are also still open to considering new designs at this stage.

Kind regards

Marta

Target Market(s)

The criminal law and law enforcement communities including solicitors, barristers, and detectives.

Industry/Entity Type

Advertising

Requirements
Must have
• Clearwater Evidence Advisors Logo
Clearwater Evidence Advisors Tagline
At least one of the images from our website
Nice to have
• Other images that fit with the picture scheme on our website and in the reference pictures attached.
Should not have
• pictures of fingerprints, deceased, glamorised crime scenes, police or vbq references.

```html
<!DOCTYPE html>
<html lang="en">
<head>
<meta charset="utf-8">
<title>Clearwater Evidence Advisors – Magnet Designs</title>
<link rel="stylesheet" href="https://fonts.googleapis.com/css2?family=Didact+Gothic&family=Open+Sans:ital,wght@1,700&display=swap">
<style>
  :root {
    --brand-blue: #1f6fb8;
    --band-blue: #2f7dc6;
    --strip-blue: #6fa6da;
    --strip-blue-light: #cfe1f3;
    --silver-dark: #c4c8d0;
    --silver-mid: #dfe2e7;
    --silver-light: #f7f8fa;
    --text-grey: #3d3d3d;
    --tagline-grey: #6b6b6b;
    --white: #ffffff;
    --card-edge: #e4e6ea;
  }
  * { box-sizing: border-box; margin: 0; padding: 0; }
  html, body {
    width: 1200px; height: 695px; overflow: hidden;
    background: var(--white);
  }
  body { position: relative; font-family: "Didact Gothic", "Century Gothic", sans-serif; color: var(--text-grey); }

  .card {
    position: absolute; width: 508px; height: 254px; overflow: hidden;
    background: var(--white); border: 1px solid var(--card-edge);
  }
  .card--curves  { left: 66px;  top: 69px; }
  .card--silver  { left: 618px; top: 67px;
    background: linear-gradient(90deg, var(--silver-dark) 0%, var(--silver-mid) 30%, var(--silver-light) 62%, var(--silver-mid) 85%, var(--silver-dark) 100%); }
  .card--band    { left: 67px;  top: 357px; }
  .card--lab     { left: 621px; top: 357px; }

  .card__art { position: absolute; inset: 0; width: 100%; height: 100%; }

  .logo { position: absolute; display: flex; align-items: center; gap: 8px; }
  .logo__dot {
    width: 48px; height: 48px; border-radius: 50%;
    background: var(--brand-blue); opacity: .85; flex: none;
  }
  .logo__name {
    font-family: "Didact Gothic", "Century Gothic", sans-serif;
    font-size: 22px; line-height: 24px; color: var(--brand-blue); font-weight: 400;
  }

  .tagline {
    position: absolute; white-space: nowrap;
    font-family: "Open Sans", Arial, sans-serif; font-style: italic; font-weight: 700;
    font-size: 15px; color: var(--tagline-grey);
  }

  .contacts { position: absolute; list-style: none; font-size: 14.5px; line-height: 22px; white-space: nowrap; }
  .contacts li { display: flex; align-items: center; gap: 7px; }
  .contacts svg { width: 11px; height: 11px; fill: var(--brand-blue); flex: none; }

  /* card: curves */
  .card--curves .logo { left: 56px; top: 19px; }
  .card--curves .tagline { left: 20px; top: 114px; }
  .card--curves .contacts { left: 110px; top: 144px; }

  /* card: silver */
  .card--silver .logo { left: 56px; top: 19px; }
  .card--silver .tagline { left: 20px; top: 110px; }
  .card--silver .contacts { left: 108px; top: 142px; }

  /* card: blue band */
  .card--band .side-strip {
    position: absolute; left: 0; top: 0; width: 118px; height: 100%;
    background: linear-gradient(180deg, var(--strip-blue) 0%, var(--strip-blue-light) 45%, var(--strip-blue-light) 60%, var(--strip-blue) 100%);
  }
  .card--band .strip-photo {
    position: absolute; left: 0; top: 152px; width: 92px; height: 92px; border-radius: 50%;
    background: radial-gradient(circle at 45% 40%, #dfe6ee 0%, #8a9db3 55%, #3c4f68 100%);
  }
  .card--band .band {
    position: absolute; left: 0; top: 93px; width: 100%; height: 28px;
    background: var(--band-blue);
  }
  .card--band .tagline { left: 32px; top: 97px; color: var(--white); }
  .card--band .logo { left: 184px; top: 10px; }
  .card--band .contacts { left: 128px; top: 138px; }

  /* card: lab header */
  .card--lab .lab-photo {
    position: absolute; left: 0; top: 0; width: 190px; height: 118px;
    background: linear-gradient(120deg, #c9ccd2 0%, #f1f2f4 45%, #d9dde3 100%);
  }
  .card--lab .logo { left: 179px; top: 30px; }
  .card--lab .tagline { left: 32px; top: 123px; }
  .card--lab .contacts { left: 88px; top: 150px; }
  .card--lab .base-bar {
    position: absolute; left: 0; bottom: 0; width: 100%; height: 8px;
    background: linear-gradient(90deg, var(--band-blue), var(--strip-blue-light) 50%, var(--band-blue));
  }
</style>
</head>
<body>

<svg width="0" height="0" style="position:absolute" aria-hidden="true">
  <symbol id="icon-phone" viewBox="0 0 12 12"><path d="M3 0.5 L4.8 3.2 L3.7 4.4 Q4.6 6.8 7.6 8.3 L8.8 7.2 L11.5 9 L10.3 11.5 Q5.8 11.8 2.5 8 Q0 4.5 0.6 1.6 Z"/></symbol>
  <symbol id="icon-mail" viewBox="0 0 12 12"><path d="M0.5 2.5 H11.5 V9.5 H0.5 Z M1.5 3.3 L6 6.6 L10.5 3.3 Z M1.3 4.3 V8.7 H10.7 V4.3 L6 7.8 Z" fill-rule="evenodd"/></symbol>
  <symbol id="icon-globe" viewBox="0 0 12 12"><circle cx="6" cy="6" r="5.2" fill="none" stroke="#1f6fb8" stroke-width="1"/><ellipse cx="6" cy="6" rx="2.3" ry="5.2" fill="none" stroke="#1f6fb8" stroke-width="0.9"/><path d="M0.8 6 H11.2 M1.6 3.4 H10.4 M1.6 8.6 H10.4" stroke="#1f6fb8" stroke-width="0.9"/></symbol>
  <symbol id="icon-pin" viewBox="0 0 12 12"><path d="M6 0.8 C3.6 0.8 2 2.6 2 4.6 C2 7.4 6 11.4 6 11.4 C6 11.4 10 7.4 10 4.6 C10 2.6 8.4 0.8 6 0.8 Z M6 3 A1.6 1.6 0 1 0 6 6.2 A1.6 1.6 0 1 0 6 3 Z" fill-rule="evenodd"/></symbol>
</svg>

<!-- Card: curves -->
<section class="card card--curves">
  <svg class="card__art" viewBox="0 0 508 254" aria-hidden="true">
    <defs>
      <linearGradient id="silver-r" x1="0" y1="0" x2="1" y2="0">
        <stop offset="0" stop-color="#f6f7f9"/><stop offset="0.5" stop-color="#d3d7de"/><stop offset="1" stop-color="#eef0f3"/>
      </linearGradient>
      <linearGradient id="silver-l" x1="0" y1="0" x2="1" y2="0">
        <stop offset="0" stop-color="#cfd3da"/><stop offset="1" stop-color="#f4f5f7"/>
      </linearGradient>
    </defs>
    <path d="M328 0 Q450 40 508 139 V0 Z" fill="url(#silver-r)"/>
    <path d="M0 111 Q40 220 178 254 H0 Z" fill="url(#silver-l)"/>
    <path d="M328 0 Q450 40 508 139" fill="none" stroke="#1f6fb8" stroke-width="3"/>
    <path d="M0 111 Q40 220 178 254" fill="none" stroke="#1f6fb8" stroke-width="3"/>
  </svg>
  <div class="logo"><span class="logo__dot"></span><span class="logo__name">Clearwater<br>Evidence Advisors</span></div>
  <p class="tagline">Forensic Science Expertise from the Crime Scene to Court</p>
  <ul class="contacts">
    <li><svg><use href="#icon-phone"/></svg>61 400 555 218</li>
    <li><svg><use href="#icon-mail"/></svg>enquiries@clearwaterevidenceadvisors.com.au</li>
    <li><svg><use href="#icon-globe"/></svg>www.clearwaterevidenceadvisors.com.au</li>
    <li><svg><use href="#icon-pin"/></svg>PO Box 3172, North Lakeside, NSW Australia 2204</li>
  </ul>
</section>

<!-- Card: silver -->
<section class="card card--silver">
  <div class="logo"><span class="logo__dot"></span><span class="logo__name">Clearwater<br>Evidence Advisors</span></div>
  <p class="tagline">Forensic Science Expertise from the Crime Scene to Court</p>
  <ul class="contacts">
    <li><svg><use href="#icon-phone"/></svg>61 400 555 218</li>
    <li><svg><use href="#icon-mail"/></svg>enquiries@clearwaterevidenceadvisors.com.au</li>
    <li><svg><use href="#icon-globe"/></svg>www.clearwaterevidenceadvisors.com.au</li>
    <li><svg><use href="#icon-pin"/></svg>PO Box 3172, North Lakeside, NSW Australia 2204</li>
  </ul>
</section>

<!-- Card: blue band -->
<section class="card card--band">
  <div class="side-strip"></div>
  <div class="strip-photo" role="img" aria-label="Close-up photograph of a laboratory microscope"></div>
  <div class="band"></div>
  <div class="logo"><span class="logo__dot"></span><span class="logo__name">Clearwater<br>Evidence Advisors</span></div>
  <p class="tagline">Forensic Science Expertise from the Crime Scene to Court</p>
  <ul class="contacts">
    <li><svg><use href="#icon-phone"/></svg>61 400 555 218</li>
    <li><svg><use href="#icon-mail"/></svg>enquiries@clearwaterevidenceadvisors.com.au</li>
    <li><svg><use href="#icon-globe"/></svg>www.clearwaterevidenceadvisors.com.au</li>
    <li><svg><use href="#icon-pin"/></svg>PO Box 3172, North Lakeside, NSW Australia 2204</li>
  </ul>
</section>

<!-- Card: lab header -->
<section class="card card--lab">
  <div class="lab-photo" role="img" aria-label="Photograph of a scientist in a lab coat looking into a microscope"></div>
  <svg class="card__art" viewBox="0 0 508 254" aria-hidden="true">
    <defs>
      <linearGradient id="header-silver" x1="0" y1="0" x2="1" y2="0">
        <stop offset="0" stop-color="#ffffff"/><stop offset="0.55" stop-color="#f1f2f5"/><stop offset="1" stop-color="#c9cdd5"/>
      </linearGradient>
    </defs>
    <path d="M212 0 Q150 40 142 118 H508 V0 Z" fill="url(#header-silver)"/>
    <path d="M212 0 Q150 40 142 118" fill="none" stroke="#1f6fb8" stroke-width="2.5"/>
  </svg>
  <div class="logo"><span class="logo__dot"></span><span class="logo__name">Clearwater<br>Evidence Advisors</span></div>
  <p class="tagline">Forensic Science Expertise from the Crime Scene to Court</p>
  <ul class="contacts">
    <li><svg><use href="#icon-phone"/></svg>61 400 555 218</li>
    <li><svg><use href="#icon-mail"/></svg>enquiries@clearwaterevidenceadvisors.com.au</li>
    <li><svg><use href="#icon-globe"/></svg>www.clearwaterevidenceadvisors.com.au</li>
    <li><svg><use href="#icon-pin"/></svg>PO Box 3172, North Lakeside, NSW Australia 2204</li>
  </ul>
  <div class="base-bar"></div>
</section>

</body>
</html>
```